K&R Flame Guard Supply Inc. needs an updated/new website design

I would like the customer to be able to see who we are, where are are, what we do and areas we cover on the first page. I would like something modern but professional. The other fire safety companies out there have very boring & unappealing websites. I want mine seem like we've got it together and to be above average in comparison. I would like the colors to go with our logo and would like to incorporate somewhere that we have been in business for over 30 years, we are family owned and operated and that we provide service to all of central Florida from Tampa to Titusville and all of Brevard county (we can take out the" all of Brevard county" but keep the " All of Central Florida from Tampa to Titusville" and just add all counties we service to the very bottom too). We are a residential and commercial fire safety equipment company. We do sales, service and installation for fire extinguishers, emergency/exit lighting, kitchen fire suppression systems, fire alarms & fire extinguisher cabinets.I have also attached some pictures that you can use to incorporate any way you would like. Here's our current website (awful I know) to get information from if needed. kandrflameguard.example

Target Market(s)

Restaurants, hotels, vacation rental properties & small businesses. Every business is required to have a fire extinguisher and exit lighting.

Industry/Entity Type

Fire Safety

Number of Pages Required

1 page

Font styles to use
Other font styles liked:
• I'm open to your suggestions

Colors

Designer to choose colors to be used in the design.

Requirements
Must have
• I would like the customer to be able to see who we are, where are are, what we do and areas we cover on the first page. I would like the colors to go with our logo and would like to incorporate somewhere that we have been in business for over 30 years, we are family owned and operated and that we provide service to all of central Florida from Tampa to Titusville and all of Brevard county (we can take out the" all of Brevard county" but keep the " All of Central Florida from Tampa to Titusville" and just add all counties we service to the very bottom too)
Nice to have
• Modern with high quality pictures
• I love the raised logo that I added in the attachments. If you could make the logo look like that in incorporate it as one of the first things you see that would be awesome!
• I would eventually like to have a portfolio of work completed on an additional page.
Should not have
• boring outdated look

```html
<!DOCTYPE html>
<html lang="en">
<head>
<meta charset="utf-8">
<title>K&amp;R Flame Guard Supply Inc.</title>
<link href="https://fonts.googleapis.com/css2?family=Montserrat:wght@400;600;700&family=Open+Sans:wght@400;600&display=swap" rel="stylesheet">
<style>
:root{
  --orange:#f7941d;
  --orange-deep:#e4661b;
  --amber:#fbb040;
  --ink:#222;
  --text:#444;
  --muted:#b3b3b3;
  --light:#efefef;
  --footer:#2a2a2a;
  --white:#fff;
}
*{margin:0;padding:0;box-sizing:border-box}
html,body{width:1200px;height:3796px;overflow:hidden}
body{position:relative;font-family:"Open Sans",Arial,sans-serif;color:var(--text);background:var(--white)}
.abs{position:absolute}
h1,h2,h3,.brand,.nav a{font-family:"Montserrat",Arial,sans-serif}

/* header */
.header{left:0;top:0;width:1200px;height:152px;background:var(--white);box-shadow:0 2px 6px rgba(0,0,0,.08);z-index:2}
.brand{left:80px;top:40px;display:flex;align-items:center;gap:14px;font-weight:700;font-size:22px;color:var(--orange-deep)}
.brand-mark{width:40px;height:40px;background:var(--orange)}
.topbar{right:80px;top:10px;display:flex;align-items:center;gap:20px;font-size:15px}
.topbar .mail{display:flex;align-items:center;gap:8px;color:var(--text)}
.topbar .call{background:var(--orange);color:var(--white);font-weight:600;padding:9px 18px;display:flex;gap:8px;align-items:center}
.nav{right:80px;top:104px;display:flex;gap:38px;font-size:15px}
.nav a{color:var(--text);text-decoration:none;font-weight:600;padding-bottom:8px}
.nav a.active{color:var(--orange);border-bottom:3px solid var(--orange)}

/* hero */
.hero{left:0;top:152px;width:1200px;height:568px;background:radial-gradient(ellipse at 50% 45%,#fbe3b5 0%,#f6b552 40%,#e8731c 80%,#b8450e 100%)}
.hero h1{left:0;top:238px;width:1200px;text-align:center;font-size:42px;font-weight:700;letter-spacing:2px;line-height:1.35;color:var(--ink)}

/* services */
.services-title{left:80px;top:832px;font-size:40px;font-weight:600;color:var(--ink)}
.services-title::after{content:"";display:block;width:70px;height:3px;background:var(--orange);margin-top:12px}
.services-sub{left:80px;top:920px;width:320px;font-size:36px;line-height:1.25;color:var(--muted);font-family:"Montserrat",Arial,sans-serif}
.tiles{left:500px;top:792px;width:620px;height:368px;display:grid;grid-template-columns:repeat(3,1fr);grid-template-rows:repeat(2,1fr);gap:2px;z-index:1}
.tile{display:flex;flex-direction:column;align-items:center;justify-content:center;gap:18px;color:var(--ink);font-size:15px}
.tile:nth-child(1){background:#c9c9c9}.tile:nth-child(2){background:#bdbdbd}.tile:nth-child(3){background:#d6d6d6}
.tile:nth-child(4){background:#d3d3d3}.tile:nth-child(5){background:#dedede}.tile:nth-child(6){background:#cbcbcb}
.view-more{right:80px;top:1128px;background:#3a3a3a;color:var(--white);font-size:14px;font-weight:600;padding:8px 14px;z-index:2}

/* who we are */
.who{left:0;top:1120px;width:1200px;height:340px;background:linear-gradient(90deg,var(--orange-deep) 0%,var(--amber) 30%,#fdd590 50%,var(--amber) 70%,var(--orange-deep) 100%)}
.who h2{left:0;top:1220px;width:1200px;text-align:center;font-size:40px;font-weight:600;color:var(--ink)}
.who-line{left:570px;top:1278px;width:60px;height:3px;background:var(--orange-deep)}
.who p{left:180px;top:1300px;width:840px;text-align:center;font-size:14px;line-height:1.7;color:#3a2a1a}

/* photos & portfolio */
.photo{background:linear-gradient(135deg,#c2281f,#e9894a 60%,#f3c9a0)}
.p1{left:80px;top:1460px;width:340px;height:320px;background:linear-gradient(135deg,#d8d4ce,#c33b2d 70%,#8f1d16)}
.p2{left:420px;top:1460px;width:360px;height:320px;background:linear-gradient(135deg,#b9201a,#e2704a 55%,#e9e2da)}
.p3{left:780px;top:1460px;width:340px;height:320px;background:linear-gradient(135deg,#f6c36a,#e8731c 60%,#c8461a)}
.p4{left:80px;top:1780px;width:340px;height:640px;background:linear-gradient(180deg,#e6e0d8,#c4241c 45%,#9b1a14)}
.p5{left:420px;top:2100px;width:360px;height:320px;background:linear-gradient(135deg,#ece8e2,#cf3a2b 60%,#a21f17)}
.p6{left:780px;top:2100px;width:340px;height:320px;background:linear-gradient(135deg,#f9d48f,#ef8a2a 55%,#9e4a22)}
.portfolio{left:420px;top:1780px;width:700px;height:320px;background:var(--white)}
.portfolio h2{left:560px;top:1854px;font-size:40px;font-weight:600;color:var(--ink)}
.portfolio-line{left:590px;top:1912px;width:70px;height:3px;background:var(--orange)}
.portfolio-sub{left:560px;top:1944px;width:480px;font-size:34px;line-height:1.3;color:var(--muted);font-family:"Montserrat",Arial,sans-serif}

/* emergency */
.emergency{left:0;top:2420px;width:1200px;height:300px;background:linear-gradient(90deg,var(--orange-deep),var(--amber) 50%,var(--orange-deep))}
.emergency h3{left:0;top:2488px;width:1200px;text-align:center;font-size:32px;font-weight:600;color:var(--ink)}
.emergency-phone{left:0;top:2566px;width:1200px;display:flex;justify-content:center;align-items:center;gap:26px;font-family:"Montserrat",Arial,sans-serif;font-size:44px;font-weight:600;color:var(--ink)}

/* testimonials */
.testimonials{left:0;top:2720px;width:1200px;height:380px;background:var(--light)}
.avatar{left:550px;top:2740px;width:100px;height:100px;border-radius:50%;background:radial-gradient(circle,#e9d8c7,#b89a84);border:4px solid var(--white)}
.client{left:0;top:2860px;width:1200px;text-align:center;font-size:16px;color:var(--ink)}
.quote{left:320px;top:2898px;width:560px;text-align:center;font-size:13px;line-height:1.7;color:#666}
.quote-mark{left:0;top:2984px;width:1200px;text-align:center;font-family:Georgia,serif;font-size:90px;line-height:1;color:#c8c8c8}
.arrow{top:2864px;width:36px;height:36px;background:#333;display:flex;align-items:center;justify-content:center}

/* contact */
.contact{left:0;top:3100px;width:1200px;height:500px;background:linear-gradient(90deg,#ffffff 0%,#ffffff 38%,#e3e5e8 60%,#b9bec4 100%)}
.contact h2{left:80px;top:3180px;font-size:40px;font-weight:600;color:var(--ink)}
.contact-line{left:80px;top:3240px;width:70px;height:3px;background:var(--orange)}
.contact-list{left:80px;top:3280px;list-style:none;font-size:15px;color:var(--text)}
.contact-list li{display:flex;align-items:flex-start;gap:14px;margin-bottom:26px;line-height:1.5}

/* footer */
.footer{left:0;top:3600px;width:1200px;height:196px;background:var(--footer);color:#ddd;font-size:14px}
.hours-l{left:80px;top:3628px}
.hours-r{right:80px;top:3628px}
.foot-nav{left:0;top:3690px;width:1200px;display:flex;justify-content:center;gap:46px}
.foot-rule{left:80px;top:3734px;width:1040px;height:1px;background:#555}
.copy{left:0;top:3752px;width:1200px;text-align:center;font-size:13px;color:#aaa}
</style>
</head>
<body>

<header class="header abs">
  <div class="brand abs"><span class="brand-mark"></span>K&amp;R Flame Guard Supply Inc.</div>
  <div class="topbar abs">
    <span class="mail">
      <svg width="20" height="14" viewBox="0 0 20 14"><rect x="1" y="1" width="18" height="12" fill="none" stroke="#f7941d" stroke-width="2"/><path d="M1 1l9 7 9-7" fill="none" stroke="#f7941d" stroke-width="2"/></svg>
      info@kandrflameguard.example
    </span>
    <span class="call">
      <svg width="16" height="16" viewBox="0 0 24 24"><path fill="#fff" d="M6.6 10.8a15 15 0 006.6 6.6l2.2-2.2c.3-.3.7-.4 1-.2 1.1.4 2.3.6 3.6.6.6 0 1 .4 1 1V20c0 .6-.4 1-1 1A17 17 0 013 4c0-.6.4-1 1-1h3.5c.6 0 1 .4 1 1 0 1.3.2 2.5.6 3.6.1.3 0 .7-.2 1z"/></svg>
      404.555.0148
    </span>
  </div>
  <nav class="nav abs">
    <a class="active">HOME</a><a>SERVICES</a><a>TESTIMONIALS</a><a>JOBS</a><a>CONTACT US</a>
  </nav>
</header>

<section class="hero abs" role="img" aria-label="Photo of a lit emergency exit sign on a ceiling surrounded by flames"></section>
<h1 class="abs" style="left:0;top:390px;width:1200px;text-align:center;font-size:42px;font-weight:700;letter-spacing:2px;line-height:1.35;color:var(--ink)">DEDICATED TO PROTECTING<br>LIFE AND PROPERTY</h1>

<h2 class="services-title abs">Services</h2>
<p class="services-sub abs">We have been in business for over 30 years</p>
<div class="tiles abs">
  <div class="tile"><svg width="40" height="40" viewBox="0 0 40 40"><rect x="4" y="8" width="32" height="24" fill="none" stroke="#222" stroke-width="3"/><path d="M12 20h16M22 14l6 6-6 6" fill="none" stroke="#222" stroke-width="3"/></svg>Exit Lighting</div>
  <div class="tile"><svg width="40" height="40" viewBox="0 0 40 40"><path d="M10 30a10 10 0 0120 0z" fill="#222"/><path d="M20 6v8M8 12l5 5M32 12l-5 5" stroke="#222" stroke-width="3"/></svg>Emergency Lighting</div>
  <div class="tile"><svg width="40" height="40" viewBox="0 0 40 40"><rect x="6" y="6" width="28" height="28" fill="none" stroke="#222" stroke-width="3"/><circle cx="20" cy="14" r="3" fill="#222"/><path d="M20 18v8M14 30l6-4 6 4" stroke="#222" stroke-width="3" fill="none"/></svg>Emergency Signage</div>
  <div class="tile"><svg width="40" height="40" viewBox="0 0 40 40"><rect x="14" y="12" width="12" height="24" rx="3" fill="#222"/><path d="M18 12V6h6M24 6l6 4" stroke="#222" stroke-width="3" fill="none"/></svg>Extinguisher Signage</div>
  <div class="tile"><svg width="40" height="40" viewBox="0 0 40 40"><path d="M8 6l6 26h12l6-26z" fill="#222"/><rect x="16" y="32" width="8" height="4" fill="#222"/></svg>Fire Hoses</div>
  <div class="tile"><svg width="40" height="40" viewBox="0 0 40 40"><path d="M20 4c6 8 10 12 10 20a10 10 0 01-20 0c0-5 3-8 5-11 1 4 3 5 5 5 0-5-1-9 0-14z" fill="#222"/></svg>Fire Retardant Blankets</div>
</div>
<div class="view-more abs">VIEW MORE ›</div>

<section class="who abs"></section>
<h2 class="abs" style="left:0;top:1212px;width:1200px;text-align:center;font-size:40px;font-weight:600;color:var(--ink)">Who we are</h2>
<div class="who-line abs"></div>
<p class="abs" style="left:180px;top:1300px;width:840px;text-align:center;font-size:14px;line-height:1.7;color:#3a2a1a">We have been providing fire protection to Central Florida for over 30 years. K&amp;R Flame Guard is family owned and operated. We provide quality service, professional fire protection and fire safety to meet the needs of our community. We provide residential and commercial fire protection to all of Brevard County and Central Florida from Tampa to Titusville. Our staff is exceptionally knowledgeable in fire safety and protection. Please feel free to contact us with any questions or concerns.</p>

<div class="abs p1" role="img" aria-label="Photo of a hand pulling a red fire alarm"></div>
<div class="abs p2" role="img" aria-label="Photo of a smoke detector with smoke"></div>
<div class="abs p3" role="img" aria-label="Photo of an exit light in front of flames"></div>
<div class="abs p4" role="img" aria-label="Photo of a red fire extinguisher mounted in a cabinet"></div>
<div class="portfolio abs"></div>
<h2 class="abs" style="left:600px;top:1850px;font-size:40px;font-weight:600;color:var(--ink)">Work Portfolio</h2>
<div class="abs" style="left:600px;top:1910px;width:70px;height:3px;background:var(--orange)"></div>
<p class="portfolio-sub abs" style="left:600px">All of Central Florida from Tampa to Titusville</p>
<div class="abs p5" role="img" aria-label="Photo of a row of fire extinguishers"></div>
<div class="abs p6" role="img" aria-label="Photo of a parking garage with fire"></div>

<section class="emergency abs"></section>
<h3 class="abs" style="left:0;top:2488px;width:1200px;text-align:center;font-size:32px;font-weight:600;color:var(--ink)">For 24 Hour Emergency Services Call Us</h3>
<div class="emergency-phone abs">
  <svg width="54" height="54" viewBox="0 0 54 54"><circle cx="27" cy="27" r="24" fill="none" stroke="#222" stroke-width="3"/><path transform="translate(15 15)" fill="#222" d="M6.6 10.8a15 15 0 006.6 6.6l2.2-2.2c.3-.3.7-.4 1-.2 1.1.4 2.3.6 3.6.6.6 0 1 .4 1 1V20c0 .6-.4 1-1 1A17 17 0 013 4c0-.6.4-1 1-1h3.5c.6 0 1 .4 1 1 0 1.3.2 2.5.6 3.6.1.3 0 .7-.2 1z"/></svg>
  1-407-555-0192
</div>

<section class="testimonials abs"></section>
<div class="avatar abs" role="img" aria-label="Client portrait"></div>
<p class="client abs">- Client Name</p>
<p class="quote abs">Lorem Ipsum is simply dummy text of the printing and typesetting industry. Lorem Ipsum has been the industry's standard dummy text ever since the 1500s, when an unknown printer took a galley of type and scrambled it to make a type specimen book. It has survived not only five centuries, but also the leap into electronic typesetting.</p>
<div class="quote-mark abs">&#8221;</div>
<div class="arrow abs" style="left:40px"><svg width="12" height="16" viewBox="0 0 12 16"><path d="M10 2L3 8l7 6" fill="none" stroke="#fff" stroke-width="3"/></svg></div>
<div class="arrow abs" style="left:1124px"><svg width="12" height="16" viewBox="0 0 12 16"><path d="M2 2l7 6-7 6" fill="none" stroke="#fff" stroke-width="3"/></svg></div>

<section class="contact abs" role="img" aria-label="Faded aerial photo of a city skyline"></section>
<h2 class="abs" style="left:80px;top:3176px;font-size:40px;font-weight:600;color:var(--ink)">Contact Us</h2>
<div class="contact-line abs"></div>
<ul class="contact-list abs">
  <li><svg width="16" height="22" viewBox="0 0 16 22"><path d="M8 0a8 8 0 00-8 8c0 6 8 14 8 14s8-8 8-14a8 8 0 00-8-8z" fill="#f7941d"/><circle cx="8" cy="8" r="3" fill="#fff"/></svg><span>Address : 2150 N Cedar Ave,<br>Oakridge FL 34700</span></li>
  <li><svg width="16" height="16" viewBox="0 0 24 24"><path fill="#f7941d" d="M6.6 10.8a15 15 0 006.6 6.6l2.2-2.2c.3-.3.7-.4 1-.2 1.1.4 2.3.6 3.6.6.6 0 1 .4 1 1V20c0 .6-.4 1-1 1A17 17 0 013 4c0-.6.4-1 1-1h3.5c.6 0 1 .4 1 1 0 1.3.2 2.5.6 3.6.1.3 0 .7-.2 1z"/></svg><span>Phone : 1-407-555-0131</span></li>
  <li><svg width="18" height="14" viewBox="0 0 20 14"><rect x="1" y="1" width="18" height="12" fill="#f7941d"/><path d="M1 1l9 7 9-7" fill="none" stroke="#fff" stroke-width="2"/></svg><span>Email : info@kandrflameguard.example</span></li>
  <li><svg width="18" height="16" viewBox="0 0 18 16"><rect x="4" y="0" width="10" height="5" fill="#f7941d"/><rect x="0" y="5" width="18" height="7" fill="#f7941d"/><rect x="4" y="10" width="10" height="6" fill="#f7941d"/></svg><span>Fax : 1-407-555-0137</span></li>
</ul>

<footer class="footer abs"></footer>
<span class="hours-l abs" style="color:#ddd;font-size:14px">Monday to Friday : 8:00-4:00</span>
<span class="hours-r abs" style="color:#ddd;font-size:14px">Saturday / Sunday : 8:00-4:00</span>
<nav class="foot-nav abs" style="color:#ddd;font-size:14px"><span>Home</span><span>Services</span><span>Testimonials</span><span>Jobs</span><span>Contact</span></nav>
<div class="foot-rule abs"></div>
<p class="copy abs">©K&amp;R FLAME GUARD SUPPLY INC. 2018 - All Rights Reserved.</p>

</body>
</html>
```